Ebook cover for online appointment scheduling software

We are operating in Brazil an online appointment scheduling software offering small business to let their clients to book online with them . We nee...

Target Market(s)

Brazilian small businesses

Industry/Entity Type

Business Software

Requirements
Must have
• see the description
Nice to have
• see the description
Should not have
• see the description

```html
<!DOCTYPE html>
<html lang="pt-BR">
<head>
<meta charset="utf-8">
<title>Agendamento manual vs Agendamento automatizado</title>
<link rel="stylesheet" href="https://fonts.googleapis.com/css2?family=Roboto:wght@300&display=swap">
<style>
  :root {
    --bg-black: #020202;
    --smoke-light: #6b6660;
    --smoke-mid: #2a2826;
    --platform-edge: #d9d6d0;
    --platform-dark: #0d0c0b;
    --title-grey: #7a7672;
  }
  html, body {
    margin: 0;
    padding: 0;
    width: 927px;
    height: 1200px;
    overflow: hidden;
    background: var(--bg-black);
  }
  .cover {
    position: relative;
    width: 927px;
    height: 1200px;
    overflow: hidden;
    background: var(--bg-black);
  }
  .arena-scene {
    position: absolute;
    inset: 0;
    background:
      linear-gradient(to bottom, transparent 0, transparent 970px, var(--platform-edge) 972px, #5a5752 980px, var(--platform-dark) 990px, #151412 1200px),
      radial-gradient(ellipse 330px 420px at 463px 800px, var(--smoke-light) 0%, var(--smoke-mid) 45%, transparent 100%),
      var(--bg-black);
  }
  .cover-title {
    position: absolute;
    top: 127px;
    left: 0;
    width: 927px;
    margin: 0;
    text-align: center;
    font-family: "Roboto", Arial, sans-serif;
    font-weight: 300;
    font-size: 63px;
    line-height: 83px;
    color: var(--title-grey);
    letter-spacing: 0;
  }
  .cover-title span { display: block; }
</style>
</head>
<body>
  <main class="cover">
    <div class="arena-scene" role="img" aria-label="Empty boxing ring with red, white and blue ropes under a smoky spotlight in a dark arena"></div>
    <h1 class="cover-title">
      <span class="title-line">Agendamento manual</span>
      <span class="title-versus">vs</span>
      <span class="title-line">Agendamento automatizado</span>
    </h1>
  </main>
</body>
</html>
```